QR TILL WORKS , CREDIT CARD PROCESSING EQUIPMENT

qrtillworks is a sub division of Tallow a credit car processing co.
dorian vell
14 cedar hollow ln
larkmoor ws 07312
suite 412

qrtillworks.example
cell 555-214-7730
office 555-861-2093
we sell pos systems to merchant who want to accept credit cards at there retail location.
black card would be nice buit open to different ideas

Target Market(s)

retail merchants

Industry/Entity Type

credit card processing

Contact Information for Business Card

card should include web site phone address

Colors

Designer to choose colors to be used in the design.

Requirements
Should not have
• red

```html
<!DOCTYPE html>
<html lang="en">
<head>
<meta charset="utf-8">
<title>QR Till Works — Business Card</title>
<link href="https://fonts.googleapis.com/css2?family=Montserrat:wght@400;600;700&display=swap" rel="stylesheet">
<style>
  :root {
    --backdrop: #3b3b3b;
    --card: #161616;
    --gold: #f2c21b;
    --white: #f4f4f4;
    --emboss: #2e2e2e;
  }
  * { box-sizing: border-box; margin: 0; padding: 0; }
  html, body { width: 1200px; height: 801px; overflow: hidden; }
  body {
    background: var(--backdrop);
    font-family: "Montserrat", sans-serif;
    position: relative;
  }
  .card {
    position: absolute;
    width: 540px;
    height: 309px;
    background: var(--card);
    border: 2px solid var(--gold);
    box-shadow: 0 14px 30px rgba(0,0,0,.45);
  }
  .card--front { left: 40px; top: 246px; }
  .card--back  { left: 620px; top: 246px; }

  .brand {
    position: absolute;
    color: var(--white);
    font-weight: 600;
    letter-spacing: 1px;
    white-space: nowrap;
  }
  .card--front .brand { right: 40px; top: 44px; font-size: 26px; }
  .card--back .brand {
    left: 0; right: 0; top: 130px;
    text-align: center;
    font-size: 40px;
    color: var(--emboss);
  }
  .divider {
    position: absolute;
    left: 28px; right: 60px; top: 176px;
    height: 1px;
    background: var(--gold);
  }
  .person {
    position: absolute;
    left: 38px; top: 146px;
    color: var(--gold);
    font-weight: 700;
    font-size: 18px;
    letter-spacing: .5px;
    text-transform: uppercase;
  }
  .contacts {
    position: absolute;
    left: 38px; top: 194px;
    list-style: none;
    color: var(--white);
    font-size: 14px;
    line-height: 22px;
  }
  .contacts li { display: flex; align-items: center; gap: 8px; }
  .contacts svg { width: 12px; height: 12px; flex: none; }
  .address {
    position: absolute;
    right: 40px; top: 196px;
    text-align: right;
    color: var(--white);
    font-size: 14px;
    line-height: 20px;
  }
</style>
</head>
<body>
  <section class="card card--front">
    <div class="brand">QR TILL WORKS</div>
    <div class="person">dorian vell</div>
    <div class="divider"></div>
    <ul class="contacts">
      <li>
        <svg viewBox="0 0 12 12"><rect x="3" y="1" width="6" height="10" rx="1" fill="none" stroke="#f2c21b" stroke-width="1.3"/></svg>
        555-214-7730
      </li>
      <li>
        <svg viewBox="0 0 12 12"><path d="M2 2c1-1 2-1 2.6 0l1 1.6c.3.6 0 1-.5 1.4 .6 1.2 1.4 2 2.6 2.6 .4-.5.8-.8 1.4-.5l1.6 1c1 .6 1 1.6 0 2.6C7 12 0 5 2 2z" fill="#f2c21b"/></svg>
        555-861-2093
      </li>
      <li>
        <svg viewBox="0 0 12 12"><circle cx="6" cy="6" r="5" fill="none" stroke="#f2c21b" stroke-width="1.3"/><path d="M1 6h10M6 1c-2.5 3-2.5 7 0 10M6 1c2.5 3 2.5 7 0 10" fill="none" stroke="#f2c21b" stroke-width="1"/></svg>
        qrtillworks.example
      </li>
    </ul>
    <div class="address">
      14 cedar hollow ln<br>
      larkmoor ws 07312<br>
      suite 412
    </div>
  </section>

  <section class="card card--back">
    <div class="brand">QR TILL WORKS</div>
  </section>
</body>
</html>
```